Marrowgate Auctions Business Cards Design Needed

I need a business card design that is modern looking - double sided (maybe just my logo on the back, but open to suggestions) - the overall design is up to you. I want it to be easy to read - not over the top flashy. I already have a company logo which I uploaded so that needs to be used. The colors of my logo are the colors I want on the card... so blue and gray (do need to match the logo colors).

Requirements
Must have
• Would like the card to be sleek, modern and easy to ready

```html
<!DOCTYPE html>
<html lang="en">
<head>
<meta charset="utf-8">
<title>Marrowgate Auctions – Business Cards</title>
<link rel="stylesheet" href="https://fonts.googleapis.com/css2?family=Montserrat:wght@600;700&family=Nunito+Sans:wght@400;600;700&display=swap">
<style>
  :root {
    --brand-blue: #2b78b8;
    --ink-gray: #4a4a4a;
    --icon-gray: #9a9a9a;
    --rule-gray: #c9c9c9;
    --paper: #ffffff;
    --stage: #2f2f2f;
  }
  * { margin: 0; padding: 0; box-sizing: border-box; }
  html, body { width: 1200px; height: 1200px; overflow: hidden; }
  body {
    background: var(--stage);
    font-family: "Nunito Sans", Arial, sans-serif;
    position: relative;
  }
  .card { position: absolute; left: 235px; width: 730px; height: 417px; }

  /* Front */
  .card-front { top: 105px; background: var(--brand-blue); color: var(--paper); }
  .front-wordmark {
    position: absolute; top: 200px; left: 0; right: 0; text-align: center;
    font-family: "Montserrat", Arial, sans-serif; font-weight: 700;
    font-size: 40px; letter-spacing: 1px; text-transform: uppercase;
  }
  .front-mark {
    position: absolute; top: 112px; left: 50%; width: 60px; height: 60px;
    margin-left: -30px; background: var(--paper);
  }
  .front-tagline {
    position: absolute; top: 282px; left: 60px; right: 60px; text-align: center;
    font-size: 21px; padding: 8px 0;
    border-top: 1px solid rgba(255,255,255,0.18);
    border-bottom: 1px solid rgba(255,255,255,0.18);
  }

  /* Back */
  .card-back { top: 670px; background: var(--paper); }
  .back-brand {
    position: absolute; left: 50px; top: 120px; width: 235px; text-align: center;
  }
  .back-mark { width: 40px; height: 40px; background: var(--brand-blue); margin: 0 auto 14px; }
  .back-wordmark {
    font-family: "Montserrat", Arial, sans-serif; font-weight: 700;
    font-size: 21px; color: var(--brand-blue); text-transform: uppercase; line-height: 1.25;
  }
  .divider {
    position: absolute; left: 326px; top: 107px; width: 2px; height: 165px;
    background: var(--rule-gray);
  }
  .contact { position: absolute; left: 372px; top: 100px; }
  .contact-name {
    font-family: "Montserrat", Arial, sans-serif; font-weight: 600;
    font-size: 32px; color: var(--brand-blue); letter-spacing: 0.5px; line-height: 1;
  }
  .contact-title { font-size: 16px; font-weight: 600; color: var(--ink-gray); margin-top: 6px; }
  .contact-list { list-style: none; margin-top: 18px; }
  .contact-list li {
    display: flex; align-items: center; gap: 12px;
    font-size: 16px; font-weight: 700; color: var(--ink-gray); height: 35px;
  }
  .contact-list svg { width: 18px; height: 18px; flex: none; }
  .back-band {
    position: absolute; left: 0; right: 0; bottom: 0; height: 47px;
    background: var(--brand-blue); color: var(--paper);
    display: flex; align-items: center; justify-content: center;
    font-size: 20px; font-weight: 700;
  }
</style>
</head>
<body>
  <section class="card card-front">
    <div class="front-mark"></div>
    <div class="front-wordmark">Marrowgate Auctions</div>
    <div class="front-tagline">Improving Charity Auctions Nationwide</div>
  </section>

  <section class="card card-back">
    <div class="back-brand">
      <div class="back-mark"></div>
      <div class="back-wordmark">Marrowgate Auctions</div>
    </div>
    <div class="divider"></div>
    <div class="contact">
      <div class="contact-name">OWEN HARTLEY</div>
      <div class="contact-title">Owner/President - Auctioneer</div>
      <ul class="contact-list">
        <li>
          <svg viewBox="0 0 24 24" fill="none" stroke="var(--icon-gray)" stroke-width="1.6"><path d="M5 3h4l2 5-2.5 1.5a11 11 0 0 0 6 6L16 13l5 2v4a2 2 0 0 1-2 2A16 16 0 0 1 3 5a2 2 0 0 1 2-2z"/></svg>
          555-014-2870
        </li>
        <li>
          <svg viewBox="0 0 24 24" fill="none" stroke="var(--icon-gray)" stroke-width="1.6"><rect x="3" y="5" width="18" height="14"/><path d="M3 5l9 8 9-8"/></svg>
          marrowgate@mail.com.
        </li>
        <li>
          <svg viewBox="0 0 24 24" fill="none" stroke="var(--icon-gray)" stroke-width="1.6"><circle cx="12" cy="12" r="9"/><path d="M3 12h18M12 3c3 3 3 15 0 18M12 3c-3 3-3 15 0 18"/></svg>
          http://bidrevival.com/
        </li>
      </ul>
    </div>
    <div class="back-band">Improving Charity Auctions Nationwide</div>
  </section>
</body>
</html>
```